Website design for online service business

The company provides the following services:
1 - consultancy services on existing products (like teamvault and deskline 354)
2 - Coaching services - Coach someone on services like using/developing features with existing products, or teach how to be more productive, or improve their business using automation, etc
3 - Training
- Online training on demand on existing products via voxora (like in Teamvault and deskline 365)
- Online courses through videos lessons and scripts by offering information products where people will need to register and pay in advance to access the online course. (productivity courses for example)

- The goal is for clients to book time with me for one of those areas without too many clicks.
- Clients will be able to Book time using an integration (it would be good to have the layout integrated with the site.) with this https://planner.brellix.example/cal/BrightPathWorks1@brightpathworks.brellix.example/slots/

- there will be areas for which i whish to build a VIP mailing list. It's referenced on the wireframes

References:
https://www.ledgerandlanternhub.example/about/about-dorvin/
https://www.quillandcompass.example/
https://teamvaultsage.example/

Target Market(s)

- Small businesses
- Freelancers

Industry/Entity Type

Business

Number of Pages Required

5+ page

Font styles to use
Sans Serif

Colors

Designer to choose colors to be used in the design.

Requirements
Must have
• Must have the design optimized to the less clicks possible to achieve any action
• The colors of the site should follow the logo (provided in attach)
• It should use other color that belong to the same pallet of colors
• Should contain colors that incentivizes people to click and book something
• Images and backgrounds should be made available
• All images sizes and colors should be provided to be able to develop the site according to the design
Nice to have
• The bookings for the time should be integrated within the design. If not possible a redirection to it can work as well.
Should not have
• Links to social media
• Pop-ups
• Intrusive navigations (like navigation bares on the left or right hand side)
• Should not be a template used by many people

```html
<!DOCTYPE html>
<html lang="en">
<head>
<meta charset="utf-8">
<title>BrightPath Works</title>
<link href="https://fonts.googleapis.com/css2?family=Poppins:ital,wght@0,400;0,500;0,600;0,700;1,700&display=swap" rel="stylesheet">
<style>
:root{
  --orange:#f0841f;
  --blue:#0c5d97;
  --ink:#1d1d1d;
  --text:#3a3a3a;
  --muted:#666;
  --footer:#efefef;
  --line:#d6d6d6;
  --white:#fff;
}
*{box-sizing:border-box;margin:0;padding:0}
html,body{width:1200px;height:2995px;overflow:hidden}
body{position:relative;font-family:'Poppins',sans-serif;color:var(--text);background:var(--white)}
.abs{position:absolute}
.center{text-align:center}
.btn{position:absolute;background:var(--orange);color:var(--white);font-weight:600;text-transform:uppercase;display:flex;align-items:center;justify-content:center;border-radius:3px}

/* hero */
.hero{left:0;top:0;width:1200px;height:598px;background:linear-gradient(160deg,#5b5149 0%,#3b3632 45%,#262422 100%)}
.hero-menu{left:1068px;top:38px;width:30px;height:30px;border:2px solid var(--white);border-radius:5px;display:flex;flex-direction:column;justify-content:center;align-items:center;gap:3px}
.hero-menu span{display:block;width:16px;height:2px;background:var(--white)}
.brand-hero{left:0;width:1200px;top:225px;color:var(--white);font-size:56px;font-weight:500;letter-spacing:6px}
.brand-hero-mark{left:570px;top:125px;width:60px;height:60px;background:var(--white);border-radius:8px}
.tagline{left:0;width:1200px;top:365px;color:var(--white);font-size:48px;font-weight:700;font-style:italic}

/* help */
.help-title{left:0;width:1200px;top:660px;font-size:34px;font-weight:700;color:var(--ink);letter-spacing:1px}
.help-col{top:765px;width:300px}
.help-art{width:180px;height:170px;margin:0 auto;border-radius:10px}
.help-col h3{margin-top:30px;font-size:24px;font-weight:500;color:var(--ink)}
.help-col p{margin-top:12px;font-size:14px;line-height:24px;color:var(--text)}
.help-col .btn{position:static;margin:20px auto 0;width:108px;height:30px;font-size:13px}

/* why */
.why{left:0;top:1200px;width:1200px;height:458px;background:var(--blue)}
.why svg{position:absolute;left:0;top:0}
.why-title{left:664px;top:1265px;font-size:34px;font-weight:700;color:var(--white);line-height:42px;letter-spacing:1px}
.why-text{left:666px;top:1365px;width:440px;font-size:14px;line-height:26px;color:var(--white);font-weight:500}
.why-btn{left:666px;top:1545px;width:124px;height:36px;background:#151515;font-size:14px}

/* questions */
.q-title{left:0;width:1200px;top:1730px;font-size:36px;font-weight:700;color:var(--ink);letter-spacing:1px}
.q-sub{left:0;width:1200px;top:1788px;font-size:14px;color:var(--muted)}
.q-box{left:307px;width:586px;height:38px;display:flex;align-items:center;justify-content:center;font-size:14px;color:var(--text);background:#f7f7f7;border:1px solid var(--line)}
.q-box.active{background:var(--orange);border-color:var(--orange);color:var(--white)}
.q-or{left:0;width:1200px;font-size:15px;color:var(--ink)}

/* cta */
.cta{left:0;top:2185px;width:1200px;height:447px;background:linear-gradient(150deg,#3a3632 0%,#23211f 55%,#1a1918 100%)}
.cta-title{left:0;width:1200px;top:2268px;font-size:36px;font-weight:700;color:var(--white)}
.cta-line{left:0;width:1200px;color:var(--white)}
.cta-btn{left:528px;top:2496px;width:144px;height:40px;font-size:17px}

/* footer */
.footer{left:0;top:2632px;width:1200px;height:303px;background:var(--footer)}
.foot-brand{left:80px;top:2720px;width:220px;font-size:26px;font-weight:600;color:var(--blue);letter-spacing:2px}
.foot-mark{left:170px;top:2688px;width:40px;height:28px}
.foot-circle{top:2827px;width:26px;height:26px;border:1.5px solid #555;border-radius:50%}
.foot-h{top:2686px;font-size:19px;font-weight:600;color:var(--ink);letter-spacing:.5px}
.news-text{left:343px;top:2732px;width:280px;font-size:12px;line-height:19px;color:var(--text)}
.news-input{left:343px;top:2784px;width:272px;height:40px;background:var(--white);border:1px solid #ccc;font-size:11px;color:#666;padding:0 14px;display:flex;align-items:center}
.news-btn{left:343px;top:2840px;width:124px;height:32px;font-size:13px;border-radius:0}
.contact-item{left:683px;font-size:13px;line-height:19px;color:var(--text);display:flex;gap:12px}
.contact-item svg{flex:none;margin-top:2px}
.links{left:973px;top:2742px;list-style:none;font-size:13px;line-height:26px;color:var(--text)}

.bottom{left:0;top:2935px;width:1200px;height:60px;border-top:1px solid var(--line);display:flex;align-items:center;justify-content:center;font-size:13px;color:var(--ink)}
</style>
</head>
<body>

<header class="abs hero" role="img" aria-label="Photo of smiling business people shaking hands across a desk"></header>
<div class="abs hero-menu"><span></span><span></span><span></span></div>
<div class="abs brand-hero-mark"></div>
<div class="abs brand-hero center">BRIGHTPATH WORKS</div>
<h1 class="abs tagline center">Because Ideas Are A Million</h1>

<h2 class="abs help-title center">HOW CAN I HELP YOU WITH YOUR IDEA?</h2>
<div class="abs help-col center" style="left:90px">
  <div class="help-art" role="img" aria-label="Illustration of a presenter beside a chart board" style="background:linear-gradient(#f1f4f7,#dfe6ec)"></div>
  <h3>I will teach you</h3>
  <p>I want to learn at my own pace. You teach me how things are done and how it works and I will do it myself.</p>
  <div class="btn">Teach me!</div>
</div>
<div class="abs help-col center" style="left:450px">
  <div class="help-art" role="img" aria-label="Illustration of a hot air balloon among clouds" style="background:linear-gradient(#f6d9cf,#bfe3e8)"></div>
  <h3>We do it together</h3>
  <p>I want to learn how it works and want to do it but I need someone that works along side with me to move forward and get it done.</p>
  <div class="btn">Let's do it!</div>
</div>
<div class="abs help-col center" style="left:810px">
  <div class="help-art" role="img" aria-label="Illustration of a woman working at a desk with a laptop" style="background:linear-gradient(#f3eee8,#e6d7c6)"></div>
  <h3>I'll do it for you</h3>
  <p>I have this great idea but I just want to have it done for me. I don't want to do it or even learn about it.</p>
  <div class="btn">Do it for me!</div>
</div>

<section class="abs why">
  <svg width="1200" height="458" viewBox="0 0 1200 458">
    <polygon points="0,0 615,0 540,458 0,458" fill="#5d6258"/>
  </svg>
  <div class="abs" role="img" aria-label="Portrait photo of the consultant outdoors on a street" style="left:0;top:0;width:540px;height:458px;clip-path:polygon(0 0,100% 0,100% 100%,0 100%)"></div>
</section>
<h2 class="abs why-title">WHY SHOULD YOU<br>HIRE MY SERVICES</h2>
<p class="abs why-text">Sed ut perspiciatis unde omnis iste natus error sit voluptatem accusantium doloremque laudantium, totam rem aperiam, eaque ipsa quae ab illo inventore veritatis et quasi architecto beatae vitae dicta sunt explicabo. Nemo enim ipsam voluptatem quia voluptas sit aspernatur aut odit aut fugit, sed quia consequuntur magni dolores</p>
<div class="btn why-btn">Read more</div>

<h2 class="abs q-title center">DO YOU HAVE ANY QUESTIONS?</h2>
<p class="abs q-sub center">It´s ok if you have questions. We haven´t worked together or met each other so how do you now if:</p>
<div class="abs q-box active" style="top:1854px">We can work together?</div>
<div class="abs q-or center" style="top:1895px">or</div>
<div class="abs q-box" style="top:1922px">understand each other</div>
<div class="abs q-or center" style="top:1963px">or</div>
<div class="abs q-box" style="top:1990px">(did i say work together?)</div>
<div class="abs q-or center" style="top:2031px">even if</div>
<div class="abs q-box" style="top:2058px">I have the experience you are looking for ?</div>

<section class="abs cta" role="img" aria-label="Dark photo of a man with glasses holding a coffee cup"></section>
<h2 class="abs cta-title center">DON´T WORRY ABOUT ANYTHING.</h2>
<p class="abs cta-line center" style="top:2330px;font-size:22px">I´m here for you !</p>
<p class="abs cta-line center" style="top:2374px;left:220px;width:760px;font-size:16px;line-height:28px;font-weight:500">Use the button bellow to book a time slot where we can have a chat about what you need help with and we will take it from there.</p>
<p class="abs cta-line center" style="top:2442px;font-size:22px">With coffee included of course!</p>
<div class="btn cta-btn">Book me</div>

<footer class="abs footer"></footer>
<div class="abs foot-mark" style="background:var(--blue);width:28px;left:172px;border-radius:3px"></div>
<div class="abs foot-brand center">BRIGHTPATH<br><span style="font-size:15px;letter-spacing:8px">WORKS</span></div>
<div class="abs foot-circle" style="left:124px"></div>
<div class="abs foot-circle" style="left:157px"></div>
<div class="abs foot-circle" style="left:190px"></div>
<div class="abs foot-circle" style="left:223px"></div>

<h4 class="abs foot-h" style="left:343px">SIGN UP FOR NEWSLETTER</h4>
<p class="abs news-text">Excepteur sint occaecat cupidatat non proident, sunt in culpa qui officia deserunt</p>
<div class="abs news-input">Enter email</div>
<div class="btn news-btn">Subscription</div>

<h4 class="abs foot-h" style="left:683px">CONTACT US</h4>
<div class="abs contact-item" style="top:2742px">
  <svg width="14" height="16" viewBox="0 0 14 16"><path d="M7 0a6 6 0 0 0-6 6c0 4.5 6 10 6 10s6-5.5 6-10a6 6 0 0 0-6-6z" fill="var(--blue)"/><circle cx="7" cy="6" r="2.3" fill="#efefef"/></svg>
  <span>BrightPathWorks 48 Alder Row,<br>Kestonbury, KB4 2LM</span>
</div>
<div class="abs contact-item" style="top:2799px">
  <svg width="14" height="14" viewBox="0 0 14 14"><path d="M3 0l2.5 3.5-1.5 2a8 8 0 0 0 4.5 4.5l2-1.5L14 11l-2 3C5 14 0 9 0 2z" fill="var(--blue)"/></svg>
  <span>Phone:&nbsp; 070 0000 4821</span>
</div>
<div class="abs contact-item" style="top:2829px">
  <svg width="14" height="12" viewBox="0 0 14 12"><rect width="14" height="12" fill="var(--blue)"/><path d="M0 0l7 6 7-6" stroke="#efefef" stroke-width="1.3" fill="none"/></svg>
  <span>Email: info@BrightPathWorks.example</span>
</div>

<h4 class="abs foot-h" style="left:973px">QUICK LINKS</h4>
<ul class="abs links">
  <li>Home</li><li>About</li><li>My services</li><li>Resources</li><li>Blog</li><li>Contact Us</li>
</ul>

<div class="abs bottom">©2018 BrightPathWorks , All Rights Reserved.</div>

</body>
</html>
```